DM - management consultant

Business card - contemporary design

Front info
Dorian Maples

(Address not necessary)
PO Box 7386
Belmont, CA 94002

(650) 555-0143
dm@dorianmapl.es

Twitter: dmq527
Facebook: /Dorian.Maples
Linkedin: /in/dorianmaples

Back or Front
www.dorianmaples.net
Facilitation & coaching, change management, strategic partnerships, business improvement

Target Market(s)

High tech businesses - mostly startups in Silicon Valley

Industry/Entity Type

Business

Font styles to use
Sans Serif

Colors

Designer to choose colors to be used in the design.

```html
<!DOCTYPE html>
<html lang="en">
<head>
<meta charset="utf-8">
<title>Dorian Maples – Business Card</title>
<link rel="stylesheet" href="https://fonts.googleapis.com/css2?family=Arimo:wght@400&display=swap">
<style>
  :root {
    --page-bg: #e8e5e1;
    --card-navy: #14213f;
    --bokeh-dark: #1f1a33;
    --bokeh-plum: #6b3a63;
    --bokeh-rose: #d9a9b8;
    --bokeh-blue: #3b4e78;
    --text-light: #ffffff;
    --divider: rgba(255, 255, 255, 0.55);
  }
  * { margin: 0; padding: 0; box-sizing: border-box; }
  html, body { width: 1200px; height: 1000px; overflow: hidden; }
  body {
    position: relative;
    background: var(--page-bg);
    font-family: "Arimo", Arial, sans-serif;
    font-weight: 400;
    color: var(--text-light);
  }
  .card {
    position: absolute;
    width: 735px;
    height: 442px;
    overflow: hidden;
  }
  .card--front { left: 252px; top: 42px; background: var(--bokeh-dark); }
  .card--back { left: 252px; top: 526px; background: var(--card-navy); }

  .front-backdrop {
    position: absolute; inset: 0;
    background:
      radial-gradient(circle at 10% 30%, rgba(255,240,245,0.85) 0%, rgba(217,169,184,0.6) 12%, rgba(107,58,99,0) 38%),
      radial-gradient(ellipse at 12% 70%, rgba(150,70,110,0.7) 0%, rgba(107,58,99,0) 45%),
      radial-gradient(ellipse at 75% 30%, rgba(110,130,175,0.55) 0%, rgba(59,78,120,0) 50%),
      linear-gradient(120deg, var(--bokeh-plum) 0%, #3a2a4f 45%, var(--bokeh-blue) 75%, var(--bokeh-dark) 100%);
  }
  .front-backdrop::after {
    content: ""; position: absolute; inset: 0;
    background: radial-gradient(ellipse at 50% 45%, rgba(0,0,0,0) 50%, rgba(10,8,20,0.6) 100%);
  }

  .holder-name {
    position: absolute;
    left: 0; width: 362px; top: 134px;
    text-align: right;
    font-size: 76px;
    font-weight: 400;
    line-height: 96px;
    letter-spacing: -1px;
  }
  .divider {
    position: absolute;
    left: 370px; top: 118px;
    width: 1px; height: 222px;
    background: var(--divider);
  }
  .contact-list { list-style: none; }
  .contact-item {
    position: absolute;
    left: 398px;
    height: 30px;
    display: flex; align-items: center;
    font-size: 20px;
    white-space: nowrap;
  }
  .contact-icon {
    width: 28px; height: 28px; margin-right: 19px;
    display: flex; align-items: center; justify-content: center;
  }
  .contact-icon svg { display: block; }
  .social-mark {
    width: 22px; height: 22px;
    border-radius: 4px;
    background: var(--text-light);
  }

  .back-decor {
    position: absolute;
    left: 440px; top: 50px; width: 230px; height: 260px;
    border-radius: 50%;
    background: radial-gradient(circle, rgba(255,255,255,0.05) 0%, rgba(255,255,255,0) 70%);
  }
  .services { list-style: none; }
  .service {
    position: absolute;
    display: flex; align-items: center;
    font-size: 21px;
    height: 30px;
    white-space: nowrap;
  }
  .service-bullet { margin-right: 14px; display: block; }
  .website {
    position: absolute;
    left: 0; right: 0; top: 386px;
    text-align: center;
    font-size: 25px;
  }
</style>
</head>
<body>
  <section class="card card--front">
    <div class="front-backdrop" role="img" aria-label="Soft out-of-focus bokeh lights in rose, plum and blue"></div>
    <h1 class="holder-name">Dorian<br>Maples</h1>
    <div class="divider"></div>
    <ul class="contact-list">
      <li class="contact-item" style="top:133px">
        <span class="contact-icon">
          <svg width="20" height="24" viewBox="0 0 20 24"><path d="M4 1 L8 1 L9 7 L6 9 C7 13 9 16 12 18 L14 15 L19 17 L19 21 C19 23 17 23 15 23 C7 21 2 13 2 5 C2 3 2 1 4 1 Z" fill="#fff"/></svg>
        </span>(650) 555-0143
      </li>
      <li class="contact-item" style="top:174px">
        <span class="contact-icon">
          <svg width="26" height="20" viewBox="0 0 26 20"><rect x="1" y="1" width="24" height="18" fill="none" stroke="#fff" stroke-width="1.8"/><path d="M1 1 L13 11 L25 1 M1 19 L10 9 M25 19 L16 9" fill="none" stroke="#fff" stroke-width="1.8"/></svg>
        </span>dm@dorianmapl.es
      </li>
      <li class="contact-item" style="top:214px">
        <span class="contact-icon"><span class="social-mark"></span></span>postlane.net/dmq527
      </li>
      <li class="contact-item" style="top:254px">
        <span class="contact-icon"><span class="social-mark"></span></span>kinnet.com/Dorian.Maples
      </li>
      <li class="contact-item" style="top:296px">
        <span class="contact-icon"><span class="social-mark"></span></span>workgraph.net/in/dorianmaples
      </li>
    </ul>
  </section>

  <section class="card card--back">
    <div class="back-decor" role="img" aria-label="Faint decorative circle pattern"></div>
    <ul class="services">
      <li class="service" style="left:82px; top:154px">
        <svg class="service-bullet" width="20" height="20" viewBox="0 0 20 20"><circle cx="10" cy="10" r="8.5" fill="none" stroke="#fff" stroke-width="1.6"/><circle cx="10" cy="10" r="4.5" fill="#fff"/></svg>Facilitation &amp; coaching
      </li>
      <li class="service" style="left:82px; top:236px">
        <svg class="service-bullet" width="20" height="20" viewBox="0 0 20 20"><circle cx="10" cy="10" r="8.5" fill="none" stroke="#fff" stroke-width="1.6"/><circle cx="10" cy="10" r="4.5" fill="#fff"/></svg>Change management
      </li>
      <li class="service" style="left:434px; top:154px">
        <svg class="service-bullet" width="20" height="20" viewBox="0 0 20 20"><circle cx="10" cy="10" r="8.5" fill="none" stroke="#fff" stroke-width="1.6"/><circle cx="10" cy="10" r="4.5" fill="#fff"/></svg>Strategic partnerships
      </li>
      <li class="service" style="left:434px; top:236px">
        <svg class="service-bullet" width="20" height="20" viewBox="0 0 20 20"><circle cx="10" cy="10" r="8.5" fill="none" stroke="#fff" stroke-width="1.6"/><circle cx="10" cy="10" r="4.5" fill="#fff"/></svg>Business improvement
      </li>
    </ul>
    <p class="website">www.dorianmaples.net</p>
  </section>
</body>
</html>
```